Web Design Project

Need a web design to be built by in-house team of developers. I need the look and feel of the site done ready for the developers to take over.

The site is a crowd funding site like www.pennyharbor.example. Our site will have all the main functions provided for on this site.
We are not looking for sophisticated investors, instead we are looking for people with an interest in investing but that need a lot of help and support through the process.

I have already obtained the logo. I attach it here.

I also want to have a coming soon page designed. I have sketched out what i want here and am uploading it in excel. this is obviously very basic and not what i will want for the main site.

colours should be light and accessible: blues, greens, yellows.

Site is to be fun and accessible.

site will have a lot of communication based aspects needed.

I am looking for a long term relationship with a designer to do this and to do many more things. I will have a lot of banners and desgin work to do here, and am looking ONLY for someone that can work on an ongoing basis (not full time, but a few hours a week).

I am also after an animation - basic 2 minute intro - not full animation, part powerpoint and part animation. I have made a separate tender for this, please quote me on it. I want the same person doing them all preferably....
Updates

Hi all

I am impressed with some of these designs. I have uploaded the wireframe of the coming soon page. 

I prefer the designs so far that are utilizing our little icons etc. 

obviously i understand you havent got root access or anything yet so are struggling to put them in, but its worth a try, some of the designs are using them well. 

i like bright colours. 

i would also show me how you are going to design other aspects eg chat box, forum page etc. 

Reason: i am going to choose a short list today and then deal only with those to get the final designs done.

Industry/Entity Type

Communication

Requirements
Must have
• the site will have all the functions of www.pennyharbor.example and www.backlantern.example.

```html
<!DOCTYPE html>
<html lang="en">
<head>
<meta charset="utf-8">
<title>Brightora – Crowdfunding</title>
<link href="https://fonts.googleapis.com/css2?family=Merriweather:wght@700;900&family=Open+Sans:wght@400;600;700&family=PT+Sans:wght@400;700&family=Marcellus&display=swap" rel="stylesheet">
<style>
:root{
  --orange:#f7a331;
  --orange-dark:#e8891a;
  --orange-light:#fbc774;
  --blue:#1d6fa3;
  --blue-dark:#0f4f7c;
  --blue-deep:#0b3f66;
  --navy:#1a4a73;
  --grey-bg:#f2f2f2;
  --grey-box:#d8d8d8;
  --grey-line:#c9c9c9;
  --text:#222;
  --footer:#1c1c1c;
  --white:#fff;
}
*{box-sizing:border-box;margin:0;padding:0}
html,body{width:822px;height:1200px;overflow:hidden}
body{position:relative;background:var(--grey-bg);font-family:"Open Sans",Verdana,sans-serif;color:var(--text)}
h1,h2,h3,h4,h5{font-weight:inherit}
.abs{position:absolute}
a{color:inherit;text-decoration:none}

/* header */
.top-strip{left:0;top:0;width:822px;height:7px;background:var(--orange)}
.header{left:0;top:7px;width:822px;height:76px;background:var(--white)}
.brand{left:95px;top:30px;display:flex;align-items:center;gap:10px}
.brand-mark{width:38px;height:38px;border-radius:50%;background:var(--orange)}
.brand-name{font-family:"Open Sans",sans-serif;font-weight:700;font-size:32px;color:var(--navy);letter-spacing:.5px}
.login{left:363px;top:7px;width:365px;height:30px;background:var(--orange);border-radius:0 0 4px 4px}
.login-field{top:6px;height:14px;background:#3c2b10;border:1px solid #6a4a1a;color:#f3d7a6;font-size:8px;padding-left:4px;line-height:12px}
.login-btn{left:200px;top:5px;width:34px;height:15px;background:#8b7148;border-radius:3px;color:#fff;font-size:8px;text-align:center;line-height:15px}
.social-signin{left:614px;top:6px;width:90px;height:12px;background:#4a6cb0;color:#fff;font-size:7px;line-height:12px;padding-left:16px;white-space:nowrap}
.social-signin::before{content:"";position:absolute;left:3px;top:2px;width:8px;height:8px;background:#fff}
.login-links{left:603px;top:22px;font-size:8.5px;color:#333;white-space:nowrap}

/* nav */
.nav{left:0;top:83px;width:822px;height:27px;background:linear-gradient(#2b86bf,#15649a)}
.nav ul{list-style:none;display:flex;position:absolute;left:95px;top:9px}
.nav li{font-family:Merriweather,serif;font-weight:700;font-size:8.6px;color:#fff;margin-right:19px}
.search{left:592px;top:88px;width:136px;height:16px;background:#fff;border-radius:3px;font-size:10px;color:#999;padding-left:6px;line-height:16px}
.search svg{position:absolute;right:4px;top:3px}

/* hero */
.hero{left:0;top:110px;width:822px;height:210px;background:radial-gradient(ellipse at 60% 30%,#2b80b6,#1a5e92 60%,#134d7c)}
.hero-title{left:93px;top:125px;font-family:Merriweather,serif;font-weight:900;font-size:19px;color:#fff}
.hero-sub{left:93px;top:152px;font-family:Merriweather,serif;font-weight:700;font-size:11.5px;color:var(--orange)}
.learn-more{left:620px;top:141px;width:108px;height:24px;border-radius:12px;background:linear-gradient(var(--orange-light),var(--orange-dark));font-family:Merriweather,serif;font-weight:700;font-size:11px;color:#3a2200;padding-left:8px;line-height:24px}
.learn-more span{position:absolute;right:5px;top:3px;width:18px;height:18px;border-radius:50%;background:#fff}
.hero-panel{left:93px;top:183px;width:249px;height:147px;background:var(--orange)}
.hero-ribbon-l{left:88px;top:320px;width:0;height:0;border-left:5px solid transparent;border-top:10px solid var(--orange-dark)}
.hero-ribbon-r{left:728px;top:320px;width:0;height:0;border-right:5px solid transparent;border-top:10px solid var(--orange-dark)}
.cta-card{left:113px;width:207px;height:61px;background:linear-gradient(90deg,#1f6fa6,#2b7fb6);border:1px solid #5a9ccc}
.cta-card h3{position:absolute;left:9px;top:9px;font-family:Merriweather,serif;font-weight:700;font-size:10px;color:#fff;line-height:12px;width:112px}
.cta-card small{position:absolute;left:9px;bottom:22px;font-family:Merriweather,serif;font-weight:700;font-size:7.5px;color:#fff}
.cta-card.tall small{bottom:8px}
.cta-art{position:absolute;right:0;top:0;width:80px;height:100%;background:linear-gradient(135deg,#cfe3f0,#8fb5cf)}
.hero-photo{left:342px;top:183px;width:386px;height:147px;background:linear-gradient(90deg,#d8cdc4,#b8b0a8 40%,#c9c3bd 70%,#e3e6ea)}

/* main card */
.main{left:93px;top:357px;width:635px;height:696px;background:#fff;box-shadow:0 0 3px rgba(0,0,0,.1)}
.section-title{left:100px;top:370px;font-size:18px;font-weight:400;color:#111}
.view-more{font-size:12px;color:var(--orange);font-weight:600}
.rule{left:100px;width:416px;height:2px;background:var(--blue)}

.pitch{width:198px;height:170px}
.pitch-name{position:absolute;left:1px;top:0;font-family:"PT Sans",sans-serif;font-size:10.5px;font-weight:700;text-decoration:underline}
.pitch-logo{position:absolute;left:0;top:14px;width:64px;height:66px;border:1px solid var(--grey-line);background:#fff}
.pitch-logo i{position:absolute;left:12px;top:13px;width:38px;height:38px}
.pitch-text{position:absolute;left:68px;top:13px;width:126px;font-family:"PT Sans",sans-serif;font-size:8.4px;line-height:8.6px;color:#222}
.pitch-text p+p{margin-top:8px}
.pitch-more{position:absolute;right:-2px;top:113px;font-family:"PT Sans",sans-serif;font-size:8.5px}
.progress{position:absolute;left:0;top:126px;width:198px;height:39px;background:var(--grey-box);border-radius:3px}
.progress-track{position:absolute;left:4px;top:4px;width:188px;height:15px;background:#fff;border:1px solid #bbb;border-radius:6px;overflow:hidden}
.progress-fill{width:40%;height:100%;background:linear-gradient(#2f88c1,#145f95)}
.progress-label{position:absolute;left:6px;top:23px;font-size:10px;color:#222}
.progress-label em{color:var(--navy);font-size:11px}

/* sidebar */
.side-box{left:532px;width:187px}
.about{top:375px;height:117px;background:linear-gradient(#d6d6d6,#c7c7c7);padding:8px 14px}
.about h4{font-size:12px;font-weight:700;color:#fff;margin-bottom:10px}
.about p{font-size:6.5px;line-height:9.5px;color:#333}
.about a{display:block;margin-top:8px;font-size:7px;font-weight:700;color:var(--orange-dark);text-decoration:underline}
.newsletter{top:500px;height:51px;background:#d6d6d6;padding:5px 8px}
.newsletter h4{font-family:Marcellus,serif;font-size:14px;color:var(--navy)}
.newsletter div{margin-top:2px;height:20px;background:#fff;border-radius:5px;font-family:Merriweather,serif;font-size:9px;color:#aaa;padding-left:6px;line-height:20px}
.blog{top:561px;height:266px;background:linear-gradient(var(--orange-light),var(--orange) 60%,var(--orange-dark))}
.blog h4{position:absolute;left:8px;top:8px;font-family:Marcellus,serif;font-size:15px;color:var(--navy)}
.blog-post{position:absolute;left:0;width:187px}
.blog-date{position:absolute;left:-7px;top:0;width:83px;height:14px;background:linear-gradient(var(--blue),var(--blue-deep));font-family:Merriweather,serif;font-size:7.5px;color:#fff;font-weight:700;padding-left:13px;line-height:14px}
.blog-line{position:absolute;left:76px;top:12px;width:84px;border-top:1px dotted #333}
.blog-post h5{position:absolute;left:26px;top:18px;width:140px;font-family:"PT Sans",sans-serif;font-size:8.6px;font-weight:700;line-height:10px}
.blog-post p{position:absolute;left:26px;top:42px;width:136px;font-family:"PT Sans",sans-serif;font-size:8.4px;line-height:9.2px}
.blog-post a{position:absolute;left:114px;top:92px;font-family:"PT Sans",sans-serif;font-size:8.5px;text-decoration:underline}
.blog-sep{position:absolute;left:26px;top:108px;width:135px;border-top:1px dotted #fff}
.payments{left:538px;top:845px;width:176px;height:37px;border:1px solid #e8c78e;background:#fff}
.payments-name{position:absolute;left:14px;top:2px;font-size:9px;font-weight:700;color:var(--navy)}
.payments-row{position:absolute;left:4px;top:15px;width:166px;height:18px;background:var(--orange);display:flex;gap:4px;padding:3px}
.payments-row i{flex:1;background:#fff;border-radius:1px}
.follow{left:594px;top:900px;font-family:Marcellus,serif;font-size:13px;color:var(--navy)}
.social{left:545px;top:923px;display:flex;gap:4px}
.social i{width:21px;height:21px;border-radius:3px;display:block}

/* featured in */
.featured-in{left:102px;top:970px;width:618px;height:63px;border-radius:5px;background:linear-gradient(var(--blue),var(--blue-deep))}
.featured-in h4{position:absolute;left:18px;top:25px;font-size:12px;font-weight:700;color:#fff}
.arrow-tab{position:absolute;top:0;width:17px;height:63px;background:linear-gradient(90deg,#d9d9d9,#fff)}
.arrow-tab svg{position:absolute;left:4px;top:25px}
.partners{position:absolute;left:131px;top:11px;display:flex;gap:15px}
.partners div{width:62px;height:42px;background:#fff;border-radius:3px;display:flex;align-items:center;justify-content:center;font-size:8.5px;font-weight:700;color:var(--navy)}

/* footer */
.footer{left:0;top:1073px;width:822px;height:127px;background:var(--footer);border-top:4px solid var(--orange)}
.footer-links{left:93px;top:1098px;font-size:7.5px;color:#fff}
.footer-legal{left:93px;top:1121px;font-size:7.5px;line-height:11.5px;color:#fff}
.copyright{left:553px;top:1132px;font-size:7.5px;color:#fff}
</style>
</head>
<body>

<div class="abs top-strip"></div>
<header class="abs header"></header>
<div class="abs brand"><span class="brand-mark"></span><span class="brand-name">Brightora</span></div>

<form class="abs login">
  <div class="abs login-field" style="left:8px;width:92px">User ID</div>
  <div class="abs login-field" style="left:104px;width:92px">Password</div>
  <div class="abs login-btn">Login</div>
</form>
<div class="abs social-signin">Sign in with Linkbook</div>
<div class="abs login-links">Register | Forgotten password</div>

<nav class="abs nav">
  <ul><li>INVEST</li><li>GET INVESTMENT</li><li>HOW IT WORKS</li><li>ABOUT US</li><li>BLOG</li><li>FORUM</li></ul>
</nav>
<div class="abs search">search
  <svg width="10" height="10" viewBox="0 0 10 10"><circle cx="4" cy="4" r="3" fill="none" stroke="#333" stroke-width="1.3"/><line x1="6.2" y1="6.2" x2="9.2" y2="9.2" stroke="#333" stroke-width="1.6"/></svg>
</div>

<section class="abs hero"></section>
<h1 class="abs hero-title">Crowdfunding with BRIGHTORA!</h1>
<p class="abs hero-sub">A new way to fund your dreams and help others to do the same.</p>
<a class="abs learn-more">Learn More <span><svg width="18" height="18" viewBox="0 0 18 18"><path d="M7 5l4 4-4 4" fill="none" stroke="#222" stroke-width="2"/></svg></span></a>

<div class="abs hero-ribbon-l"></div>
<div class="abs hero-ribbon-r"></div>
<div class="abs hero-panel"></div>
<a class="abs cta-card" style="top:193px"><h3>Invest In a Business</h3><small>Click Here to Read more</small><span class="cta-art" role="img" aria-label="Rising stacks of coins with growth arrow"></span></a>
<a class="abs cta-card tall" style="top:260px"><h3>Get Investment for your Business</h3><small>Click Here to Read more</small><span class="cta-art" role="img" aria-label="Rising stacks of coins with growth arrow"></span></a>
<div class="abs hero-photo" role="img" aria-label="Group of smiling business people with the caption A new way to invest"></div>

<main class="abs main"></main>
<h2 class="abs section-title">Featured pitches</h2>
<a class="abs view-more" style="left:447px;top:379px">View more +</a>
<div class="abs rule" style="top:393px"></div>

<article class="abs pitch" style="left:101px;top:405px">
  <span class="pitch-name">Company Name:</span>
  <div class="pitch-logo"><i style="background:#1f3f8f"></i></div>
  <div class="pitch-text"><p>Lorem Ipsum is simply dummy text of the printing and typesetting industry. Lorem Ipsum has been the industry's standard dummy text ever since the 1500s, when an unknown printer took a galley of type and</p><p>Lorem Ipsum is simply dummy text of the printing and typesetting industry. Lorem Ipsum ....</p></div>
  <a class="pitch-more">Read more</a>
  <div class="progress"><div class="progress-track"><div class="progress-fill"></div></div><div class="progress-label"><em>40%</em> invested so far</div></div>
</article>
<article class="abs pitch" style="left:318px;top:405px">
  <span class="pitch-name">Company Name:</span>
  <div class="pitch-logo"><i style="background:#d3202c"></i></div>
  <div class="pitch-text"><p>Lorem Ipsum is simply dummy text of the printing and typesetting industry. Lorem Ipsum has been the industry's standard dummy text ever since the 1500s, when an unknown printer took a galley of type and</p><p>Lorem Ipsum is simply dummy text of the printing and typesetting industry. Lorem Ipsum ....</p></div>
  <a class="pitch-more">Read more</a>
  <div class="progress"><div class="progress-track"><div class="progress-fill"></div></div><div class="progress-label"><em>40%</em> invested so far</div></div>
</article>
<article class="abs pitch" style="left:101px;top:585px">
  <span class="pitch-name">Company Name:</span>
  <div class="pitch-logo"><i style="background:#2b3f8f;border-radius:50%"></i></div>
  <div class="pitch-text"><p>Lorem Ipsum is simply dummy text of the printing and typesetting industry. Lorem Ipsum has been the industry's standard dummy text ever since the 1500s, when an unknown printer took a galley of type and</p><p>Lorem Ipsum is simply dummy text of the printing and typesetting industry. Lorem Ipsum ....</p></div>
  <a class="pitch-more">Read more</a>
  <div class="progress"><div class="progress-track"><div class="progress-fill"></div></div><div class="progress-label"><em>40%</em> invested so far</div></div>
</article>
<article class="abs pitch" style="left:318px;top:585px">
  <span class="pitch-name">Company Name:</span>
  <div class="pitch-logo"><i style="background:#e9751c"></i></div>
  <div class="pitch-text"><p>Lorem Ipsum is simply dummy text of the printing and typesetting industry. Lorem Ipsum has been the industry's standard dummy text ever since the 1500s, when an unknown printer took a galley of type and</p><p>Lorem Ipsum is simply dummy text of the printing and typesetting industry. Lorem Ipsum ....</p></div>
  <a class="pitch-more">Read more</a>
  <div class="progress"><div class="progress-track"><div class="progress-fill"></div></div><div class="progress-label"><em>40%</em> invested so far</div></div>
</article>
<article class="abs pitch" style="left:101px;top:765px">
  <span class="pitch-name">Company Name:</span>
  <div class="pitch-logo"><i style="background:#23307a;border-radius:50%"></i></div>
  <div class="pitch-text"><p>Lorem Ipsum is simply dummy text of the printing and typesetting industry. Lorem Ipsum has been the industry's standard dummy text ever since the 1500s, when an unknown printer took a galley of type and</p><p>Lorem Ipsum is simply dummy text of the printing and typesetting industry. Lorem Ipsum ....</p></div>
  <a class="pitch-more">Read more</a>
  <div class="progress"><div class="progress-track"><div class="progress-fill"></div></div><div class="progress-label"><em>40%</em> invested so far</div></div>
</article>
<article class="abs pitch" style="left:318px;top:765px">
  <span class="pitch-name">Company Name:</span>
  <div class="pitch-logo"><i style="background:#333"></i></div>
  <div class="pitch-text"><p>Lorem Ipsum is simply dummy text of the printing and typesetting industry. Lorem Ipsum has been the industry's standard dummy text ever since the 1500s, when an unknown printer took a galley of type and</p><p>Lorem Ipsum is simply dummy text of the printing and typesetting industry. Lorem Ipsum ....</p></div>
  <a class="pitch-more">Read more</a>
  <div class="progress"><div class="progress-track"><div class="progress-fill"></div></div><div class="progress-label"><em>40%</em> invested so far</div></div>
</article>

<div class="abs rule" style="top:936px"></div>
<a class="abs view-more" style="left:447px;top:939px">View more +</a>

<aside class="abs side-box about">
  <h4>What is crowdfunding?</h4>
  <p>Crowdfunding is the new way for a community of like minded people to network and pool their money and knowledge together. Pennyharbor provides a platform for entrepreneurs of start-ups and established businesses to connect with potential investors.</p>
  <a>» Learn more</a>
</aside>
<aside class="abs side-box newsletter"><h4>Newsletter</h4><div>Subscribe Here...</div></aside>
<aside class="abs side-box blog">
  <h4>Our Latest Blog</h4>
  <div class="blog-post" style="top:33px">
    <span class="blog-date">12-10-2011</span><span class="blog-line"></span>
    <h5>Lorem Ipsum is simply dummy text of</h5>
    <p>the printing and typesetting industry. Lorem Ipsum has been the industry's standard dummy text ever since the 1500s, when an unknown ....</p>
    <a>Read more</a>
    <span class="blog-sep"></span>
  </div>
  <div class="blog-post" style="top:152px">
    <span class="blog-date">12-10-2011</span><span class="blog-line"></span>
    <h5>Lorem Ipsum is simply dummy text of</h5>
    <p>the printing and typesetting industry. Lorem Ipsum has been the industry's standard dummy text ever since the 1500s, when an unknown ....</p>
    <a>Read more</a>
  </div>
</aside>
<div class="abs payments"><span class="payments-name">Tallypost</span><div class="payments-row"><i></i><i></i><i></i><i></i><i></i><i></i></div></div>
<div class="abs follow">Follow Us</div>
<div class="abs social">
  <i style="background:#3b5b9a"></i><i style="background:#4bb3e0"></i><i style="background:#1b7bb5"></i><i style="background:#f08a24"></i><i style="background:#c4302b"></i><i style="background:#f57d00"></i><i style="background:#12a5e0"></i>
</div>

<section class="abs featured-in">
  <h4>Featured In:</h4>
  <span class="arrow-tab" style="left:102px"><svg width="9" height="13" viewBox="0 0 9 13"><path d="M7 1L2 6.5 7 12" fill="none" stroke="#1d6fa3" stroke-width="2.5"/></svg></span>
  <div class="partners"><div>Norvale</div><div>Slatehub</div><div>Cobaltline</div><div>Parvenna</div><div>Kestrel</div><div>Solmira</div></div>
  <span class="arrow-tab" style="left:593px;background:linear-gradient(270deg,#d9d9d9,#fff)"><svg width="9" height="13" viewBox="0 0 9 13"><path d="M2 1l5 5.5L2 12" fill="none" stroke="#1d6fa3" stroke-width="2.5"/></svg></span>
</section>

<footer class="abs footer"></footer>
<div class="abs footer-links">Contact us &nbsp;|&nbsp; Terms of Use &nbsp;|&nbsp; Privacy policy &nbsp;|&nbsp; Sitemap &nbsp;|&nbsp; FAQ &nbsp;|&nbsp; Partnership Opportunities &nbsp;|&nbsp; Press</div>
<div class="abs footer-legal">Pennyharbor is a registered trademark of Brightora Limited<br>This website has been approved as a financial promotion by Marlow Ashby which is authorised and<br>regulated by the Financial Standards Office.</div>
<div class="abs copyright">Copyright 2011 &nbsp;Brightora Limited All right reserved.</div>

</body>
</html>
```